Business Card Design Project - bel soravin group

dear Sirs

we need business card design for our group ( BEL Soravin Group ) , i have got the Logo design of our group from pixel harbor in previous , so all need details relating to our group i think available with you, as well as the the chosen logo design

we hope to provide us with business card logo that to be appropaite and satisfactory to us .

thanks

note : logo design of our group is attached .
Updates

Reason: please extend the deadline of my project for additional 15 days because i didn't received appropriate design for our gruop yet . kindly beaware that i have received 77 design till now , supossed to send me 200-250 design at least . thanks

Target Market(s)

contents
-

name : Korvan EL Mistrani

position : Operation Manager

Industry/Entity Type

Business

Requirements
Must have

• person name

group logo
Nice to have
• logo color matching with back background

```html
<!DOCTYPE html>
<html lang="en">
<head>
<meta charset="utf-8">
<title>BEL Soravin Group – Business Card</title>
<link rel="stylesheet" href="https://fonts.googleapis.com/css2?family=Didact+Gothic&family=Niconne&display=swap">
<style>
  :root {
    --card-top: #3384c5;
    --card-mid: #a6bfe3;
    --card-bottom: #ffffff;
    --bevel-top: #aec7e6;
    --bevel-left: #8db1de;
    --bevel-right-top: #4a7cc4;
    --bevel-right-bottom: #c2b8dc;
    --bevel-bottom: #ab9fcd;
    --brand-blue: #2d5ca6;
    --name-lilac: #7f80b9;
    --ink: #111111;
    --rule: #555a60;
  }
  html, body {
    margin: 0;
    padding: 0;
    width: 1200px;
    height: 720px;
    overflow: hidden;
    background: #ffffff;
  }
  .card {
    position: relative;
    width: 1200px;
    height: 720px;
    font-family: "Didact Gothic", "Century Gothic", sans-serif;
    color: var(--ink);
  }
  .card__frame {
    position: absolute;
    inset: 0;
  }
  .card__text {
    position: absolute;
    margin: 0;
    line-height: 1;
    white-space: nowrap;
  }
  .brand {
    position: absolute;
    left: 90px;
    top: 118px;
    display: flex;
    align-items: center;
    gap: 16px;
  }
  .brand__mark {
    width: 34px;
    height: 34px;
    background: var(--brand-blue);
  }
  .brand__name {
    margin: 0;
    font-size: 44px;
    line-height: 1;
    color: var(--brand-blue);
    letter-spacing: 1px;
  }
  .contact-label {
    font-size: 25px;
  }
  .person-name {
    right: 221px;
    top: 258px;
    font-family: "Niconne", cursive;
    font-size: 72px;
    color: var(--name-lilac);
    letter-spacing: 1px;
  }
  .person-role {
    right: 222px;
    top: 336px;
    font-size: 26px;
  }
  .divider {
    position: absolute;
    left: 61px;
    top: 487px;
    width: 1097px;
    height: 2px;
    background: var(--rule);
  }
</style>
</head>
<body>
  <main class="card">
    <svg class="card__frame" width="1200" height="720" viewBox="0 0 1200 720" aria-hidden="true">
      <defs>
        <linearGradient id="face" x1="0" y1="0" x2="0" y2="1">
          <stop offset="0" stop-color="var(--card-top)"/>
          <stop offset="0.6" stop-color="var(--card-mid)"/>
          <stop offset="1" stop-color="var(--card-bottom)"/>
        </linearGradient>
        <linearGradient id="bevelRight" x1="0" y1="0" x2="0" y2="1">
          <stop offset="0" stop-color="var(--bevel-right-top)"/>
          <stop offset="1" stop-color="var(--bevel-right-bottom)"/>
        </linearGradient>
        <linearGradient id="bevelLeft" x1="0" y1="0" x2="0" y2="1">
          <stop offset="0" stop-color="var(--bevel-left)"/>
          <stop offset="1" stop-color="#e6e8f5"/>
        </linearGradient>
      </defs>
      <rect x="18" y="18" width="1164" height="684" fill="url(#face)"/>
      <polygon points="0,0 1200,0 1182,18 18,18" fill="var(--bevel-top)"/>
      <polygon points="0,0 18,18 18,702 0,720" fill="url(#bevelLeft)"/>
      <polygon points="1200,0 1200,720 1182,702 1182,18" fill="url(#bevelRight)"/>
      <polygon points="0,720 18,702 1182,702 1200,720" fill="var(--bevel-bottom)"/>
    </svg>

    <div class="brand">
      <span class="brand__mark" aria-hidden="true"></span>
      <p class="brand__name">BEL Soravin Group</p>
    </div>

    <p class="card__text contact-label" style="left:873px; top:76px;">Tel:</p>
    <p class="card__text contact-label" style="left:871px; top:125px;">Mobile:</p>

    <h1 class="card__text person-name">Korvan EL Mistrani</h1>
    <p class="card__text person-role">Operation Manager</p>

    <div class="divider" aria-hidden="true"></div>

    <p class="card__text contact-label" style="left:108px; top:554px;">Email address:</p>
    <p class="card__text contact-label" style="left:110px; top:608px;">Fax:</p>
    <p class="card__text contact-label" style="left:792px; top:544px;">Web site:</p>
    <p class="card__text contact-label" style="left:798px; top:608px;">PO.Box:</p>
  </main>
</body>
</html>
```